Manufacturing company needs new business card.

I need a unique Business Card that will truly stand out. Nothing too busy. Simple is good, right? Not looking for a standard design either. No cookie cutter layout. I am just looking for something interesting and a bit different. Does't have to completely off the wall crazy, just not your run of the mill business card. Clean and modern with a touch of industrial.

Target Market(s)

Air conditioning industry, Architects, builders.

Industry/Entity Type

Business

Contact Information for Business Card

Details to be included on card are:

Peter Vance
Managing Director

T: 1300 847 519
M: 0428 593 174
W: www.brenvaleworks.com.au
E: peter.vance@brenvaleworks.com.au
A: 58 Harwick Lane, Sydney NSW 2000

Font styles to use
Sans Serif

Colors
0355a3
848484
fbfbfb

Requirements
Must have
• Card design must be landscape.

```html
<!DOCTYPE html>
<html lang="en">
<head>
<meta charset="utf-8">
<title>Brenvale Works – Business Card</title>
<link rel="stylesheet" href="https://fonts.googleapis.com/css2?family=Source+Sans+3:wght@400;600;700&display=swap">
<style>
  :root {
    --brand-blue: #0355a3;
    --back-blue: #1f4fa3;
    --ink-grey: #5a5a5a;
    --rule-grey: #848484;
    --paper: #fbfbfb;
    --stage: #e4e2df;
  }
  * { box-sizing: border-box; margin: 0; padding: 0; }
  html, body { width: 1200px; height: 987px; overflow: hidden; }
  body {
    background: var(--stage);
    font-family: "Source Sans 3", Arial, sans-serif;
    position: relative;
  }
  .card {
    position: absolute;
    left: 293px;
    width: 615px;
    height: 351px;
    box-shadow: 0 2px 6px rgba(0,0,0,.18);
  }
  .card--front { top: 130px; background: var(--paper); }
  .card--back { top: 506px; background: var(--back-blue); }

  .brand {
    position: absolute;
    display: flex;
    align-items: center;
    gap: 10px;
    font-weight: 600;
    letter-spacing: -0.2px;
  }
  .card--front .brand {
    top: 34px;
    right: 34px;
    color: var(--brand-blue);
    font-size: 30px;
  }
  .brand__square {
    width: 22px; height: 22px;
    background: var(--brand-blue);
  }

  .person {
    position: absolute;
    left: 33px;
    top: 208px;
  }
  .person__name {
    font-size: 22px;
    font-weight: 600;
    color: var(--brand-blue);
    letter-spacing: .3px;
    line-height: 1;
  }
  .person__role {
    margin-top: 6px;
    font-size: 17px;
    color: var(--ink-grey);
    line-height: 1;
  }
  .rule {
    position: absolute;
    left: 33px;
    right: 33px;
    top: 266px;
    border-top: 1px solid var(--rule-grey);
  }
  .contacts {
    position: absolute;
    left: 33px;
    right: 33px;
    top: 278px;
    font-size: 16px;
    color: #333;
    line-height: 26px;
  }
  .contacts__row { display: flex; align-items: center; white-space: nowrap; }
  .contacts__item { display: inline-flex; align-items: center; gap: 4px; margin-right: 8px; }
  .contacts__sep { margin: 0 8px 0 4px; }
  .icon { width: 14px; height: 14px; fill: var(--brand-blue); flex: none; }

  .card--back .brand {
    right: 34px;
    top: 216px;
    color: #fff;
    font-size: 24px;
  }
  .card--back .brand__square { background: #fff; width: 16px; height: 16px; }
  .back__web {
    position: absolute;
    right: 34px;
    top: 254px;
    color: #fff;
    font-size: 16px;
  }
</style>
</head>
<body>
  <section class="card card--front">
    <div class="brand"><span class="brand__square"></span>Brenvale Works</div>

    <div class="person">
      <div class="person__name">PETER VANCE</div>
      <div class="person__role">Managing Director</div>
    </div>

    <div class="rule"></div>

    <div class="contacts">
      <div class="contacts__row">
        <span class="contacts__item">58 Harwick Lane, Sydney NSW 2000</span><span class="contacts__sep">|</span>
        <span class="contacts__item">
          <svg class="icon" viewBox="0 0 24 24"><path d="M6.6 10.8a15.1 15.1 0 0 0 6.6 6.6l2.2-2.2c.3-.3.7-.4 1-.2 1.1.4 2.3.6 3.6.6.6 0 1 .4 1 1V20c0 .6-.4 1-1 1A17 17 0 0 1 3 4c0-.6.4-1 1-1h3.5c.6 0 1 .4 1 1 0 1.3.2 2.5.6 3.6.1.3 0 .7-.2 1z"/></svg>
          1300 847 519
        </span>
        <span class="contacts__item">
          <svg class="icon" viewBox="0 0 24 24"><path d="M7 1h10a2 2 0 0 1 2 2v18a2 2 0 0 1-2 2H7a2 2 0 0 1-2-2V3a2 2 0 0 1 2-2zm0 3v14h10V4zm5 15.5a1.2 1.2 0 1 0 0 2.4 1.2 1.2 0 0 0 0-2.4z"/></svg>
          0428 593 174
        </span>
      </div>
      <div class="contacts__row">
        <span class="contacts__item">
          <svg class="icon" viewBox="0 0 24 24"><path d="M2 5h20v14H2zm2 2v.5l8 5 8-5V7zm0 2.8V17h16V9.8l-8 5z"/></svg>
          peter.vance@brenvaleworks.com.au
        </span>
        <span class="contacts__item">
          <svg class="icon" viewBox="0 0 24 24"><circle cx="12" cy="12" r="10"/><path d="M2 12h20M12 2c3 3 3 17 0 20M12 2c-3 3-3 17 0 20" stroke="#fff" stroke-width="1.4" fill="none"/></svg>
          brenvaleworks.com.au
        </span>
      </div>
    </div>
  </section>

  <section class="card card--back">
    <div class="brand"><span class="brand__square"></span>Brenvale Works</div>
    <div class="back__web">www.brenvaleworks.com.au</div>
  </section>
</body>
</html>
```